Infographic & Data Visualisation Design for – Australia’s Yearly Harmwatch Review 2026

About Carrowby Institute: Carrowby Institute is an independent non-profit public health organization. We produce Australia’s Yearly Harmwatch Review, which translates verified national mortality data into actionable insights for policymakers, journalists, healthcare workers, and the general public.

Project Goal: We need a suite of high-impact, clean, and authoritative infographics and data visualisations created for Australia’s Yearly Harmwatch Review 2026.

What We Are Providing:

Full Dataset (.xlsx): Complete Excel file containing all 2026 report data.

Data & Chart Guidance Doc (.docx): A summary document detailing each dataset, the core takeaway, and our initial recommendations for chart types (e.g., line graphs, horizontal bar charts, donut charts, metric tiles).

Carrowby Institute Brand Book (.pdf): Complete brand guidelines covering fonts, colors, line weights, and imagery. These guidelines and in particular colours should be used across the infographics.

Previous Year Reference: You can view how last year’s report and graphics here: https://www.carrowby-example.org.au/australias-yearly-harmwatch-review-2025/

Designer Input & Creative Freedom: While we have provided a guide suggesting specific chart types for each dataset, we are not data visualisation experts - you are! We are very open to your creative ideas, structural suggestions, and design expertise. If you identify a clearer, more engaging, or visually compelling way to illustrate a specific dataset, we welcome your input.

Required Deliverables:

Master Report Infographics: High-resolution, print/PDF-ready A4 vector graphics for the formal report publication (Delivered as vector AI/EPS and high-res PDF/PNG).

Web Assets: Web-optimized PNG/SVG files with transparent or brand backgrounds.

Social Media Adaptations: 1:1 (Square) and 4:5 / 9:16 (Vertical) graphic cards for Pictoral, WorkMesh, Chatterly, and X.
Updates

Deadline was too tight - have extended it to ensure the designers have enough time to do the job.

Target Market(s)

Policy makers, journalists, health sector professionals, frontline workers, and the general public.

Industry/Entity Type

Drug/Government/Not for Profit

Font styles to use
Sans Serif
Other font styles liked:
• Brand Fonts: Use any or a combination of: Host Grotesk or Libre Baskerville or Poppins or Calibri Light

Colors

Designer to choose colors to be used in the design.

Requirements
Must have
• The ability to create Infographics, graphs of all kinds from data that we have given.
Nice to have
• Help with choosing what infographics/graphs/donuts graphs etc will be best to visualise the data.
Should not have
• A designer who has not made graphs or infographics from Data.

```html
<!DOCTYPE html>
<html lang="en">
<head>
<meta charset="utf-8">
<title>Australia’s Yearly Harmwatch Review 2026 — Infographic Suite</title>
<link href="https://fonts.googleapis.com/css2?family=Host+Grotesk:wght@400;500;600&family=Libre+Baskerville:ital,wght@0,400;1,400&display=swap" rel="stylesheet">
<style>
  :root {
    --navy: #13294f;
    --blue: #4a8bcb;
    --orange: #f47a42;
    --violet: #5a6bb5;
    --teal-light: #7fcbdd;
    --sky: #a9c4e4;
    --slate: #2c5268;
    --maroon: #6b1747;
    --green: #1a7a40;
    --purple: #7b3fa6;
    --charcoal: #2b2b2b;
    --ink: #1b1b1b;
    --track: #e6e6e6;
    --page: #ffffff;
    --backdrop-a: #93a8c8;
    --backdrop-b: #7f96b8;
  }
  * { margin: 0; padding: 0; box-sizing: border-box; }
  html, body { width: 883px; height: 1200px; overflow: hidden; }
  body {
    background: linear-gradient(180deg, var(--backdrop-a), var(--backdrop-b) 50%, var(--backdrop-a));
    position: relative;
    font-family: "Host Grotesk", Arial, sans-serif;
  }
  .sheet {
    position: absolute;
    width: 257px;
    height: 363px;
    background: var(--page);
  }
  .sheet svg { display: block; width: 257px; height: 363px; }
  .col-1 { left: 45px; } .col-2 { left: 313px; } .col-3 { left: 582px; }
  .row-1 { top: 44px; } .row-2 { top: 419px; } .row-3 { top: 793px; }
  .title { font-family: "Libre Baskerville", Georgia, serif; font-size: 16.5px; fill: var(--ink); text-anchor: middle; }
  .ring-caption { font-family: "Libre Baskerville", Georgia, serif; font-size: 10.5px; fill: var(--ink); text-anchor: middle; }
  .hub-title { font-family: "Libre Baskerville", Georgia, serif; font-size: 16px; fill: #ffffff; text-anchor: middle; }
  .it { font-style: italic; }
  .sans { font-family: "Host Grotesk", Arial, sans-serif; }
  .mid { text-anchor: middle; }
  .axis-label { font-family: "Host Grotesk", Arial, sans-serif; font-size: 8.5px; fill: var(--ink); }
  .point-label { font-family: "Host Grotesk", Arial, sans-serif; font-size: 8px; fill: var(--ink); text-anchor: middle; }
  .tiny { font-family: "Host Grotesk", Arial, sans-serif; font-size: 5.5px; fill: var(--ink); }
  .leader { fill: none; stroke: #9a9a9a; stroke-width: 0.8; }
  .grid { stroke: #9a9a9a; stroke-width: 0.8; stroke-dasharray: 2 2; }
  .dash-outline { fill: none; stroke: var(--navy); stroke-width: 1.2; stroke-dasharray: 3 3; }
</style>
</head>
<body>

<!-- Total deaths -->
<section class="sheet col-1 row-1">
  <svg viewBox="0 0 480 678" aria-labelledby="t1">
    <text class="title" id="t1"><tspan x="240" y="84"><tspan class="it">Total Death </tspan><tspan class="it" fill="#f47a42">(2,595)</tspan> – Number of</tspan><tspan x="240" y="102">overdose deaths in Australia in 2024</tspan></text>
    <g class="donut" transform="rotate(-90 125 236)" fill="none" stroke-width="17">
      <circle cx="125" cy="236" r="62" stroke="var(--navy)" stroke-dasharray="163.6 389.6"/>
      <circle cx="125" cy="236" r="62" stroke="var(--violet)" stroke-dasharray="0 163.6 50.6 389.6"/>
      <circle cx="125" cy="236" r="62" stroke="var(--blue)" stroke-dasharray="0 214.2 85.7 389.6"/>
      <circle cx="125" cy="236" r="62" stroke="var(--orange)" stroke-dasharray="0 299.9 89.7 389.6"/>
    </g>
    <text class="sans mid" x="125" y="246" font-size="27" font-weight="500" fill="var(--navy)">2,595</text>
    <rect x="250" y="176" width="166" height="121" rx="10" fill="none" stroke="#9aa9c4" stroke-width="1.2"/>
    <path d="M266 197 q4 -5 8 0 q4 -5 8 0 l-8 8 z" fill="none" stroke="var(--orange)" stroke-width="1.2"/>
    <text class="sans" x="288" y="198" font-size="9" fill="var(--ink)">Unintentional overdose</text>
    <text class="sans" x="288" y="209" font-size="9" fill="var(--ink)">deaths</text>
    <text class="sans" x="262" y="246" font-size="38" font-weight="500" fill="var(--navy)">78%</text>
    <text class="sans" x="343" y="245" font-size="7" fill="var(--ink)">or</text>
    <text class="sans" x="262" y="284" font-size="38" font-weight="500" fill="var(--orange)">1768</text>
    <text class="sans" x="355" y="282" font-size="8" fill="var(--ink)">deaths</text>
    <defs>
      <linearGradient id="mapTone" x1="0" y1="0" x2="1" y2="1">
        <stop offset="0" stop-color="#4a8bcb"/>
        <stop offset="0.5" stop-color="#5a6bb5"/>
        <stop offset="1" stop-color="#13294f"/>
      </linearGradient>
    </defs>
    <rect role="img" aria-label="Map of Australia with each state shaded by overdose deaths" x="66" y="326" width="346" height="326" rx="40" fill="url(#mapTone)"/>
  </svg>
</section>

<!-- Overdose vs population -->
<section class="sheet col-2 row-1">
  <svg viewBox="0 0 480 678" aria-labelledby="t2">
    <text class="title" id="t2"><tspan x="240" y="84" class="it">Overdose vs. Population -</tspan><tspan x="240" y="102">Unintentional overdose deaths compared with</tspan><tspan x="240" y="120">population growth 2001 – 2024</tspan></text>
    <text class="sans" font-size="11" fill="var(--ink)"><tspan x="68" y="311">Unintentional overdose</tspan><tspan x="68" y="324">deaths compared with</tspan><tspan x="68" y="338">population growth</tspan><tspan x="68" y="351">2001 – 2024</tspan></text>
    <rect x="45" y="403" width="180" height="78" rx="39" fill="var(--blue)"/>
    <rect x="150" y="403" width="60" height="78" fill="var(--blue)"/>
    <text class="sans mid" x="125" y="439" font-size="29" fill="#fff">2,091</text>
    <text class="sans mid" x="125" y="455" font-size="10.5" fill="#fff">Unintentional</text>
    <text class="sans mid" x="125" y="468" font-size="10.5" fill="#fff">overdose deaths</text>
    <rect x="260" y="292" width="175" height="78" rx="39" fill="var(--orange)"/>
    <rect x="260" y="292" width="60" height="78" fill="var(--orange)"/>
    <text class="sans mid" x="352" y="337" font-size="25" fill="#fff">27194300</text>
    <text class="sans mid" x="352" y="353" font-size="10.5" fill="#fff">Population of Australia</text>
    <rect x="204" y="275" width="22" height="222" rx="11" fill="#fff" stroke="var(--blue)" stroke-width="3"/>
    <line x1="215" y1="290" x2="215" y2="485" stroke="var(--blue)" stroke-width="1.5"/>
    <circle cx="215" cy="327" r="5" fill="var(--blue)"/>
    <rect x="254" y="275" width="22" height="222" rx="11" fill="#fff" stroke="var(--orange)" stroke-width="3"/>
    <line x1="265" y1="290" x2="265" y2="485" stroke="var(--orange)" stroke-width="1.5"/>
    <circle cx="265" cy="388" r="5" fill="var(--orange)"/>
  </svg>
</section>

<!-- Overdose vs road toll -->
<section class="sheet col-3 row-1">
  <svg viewBox="0 0 480 678" aria-labelledby="t3">
    <text class="title" id="t3"><tspan x="240" y="84"><tspan class="it">Overdose vs. Road Toll</tspan> - Overdose deaths</tspan><tspan x="240" y="102">compared with the road toll 2001 – 2024</tspan></text>
    <g class="arrow-road">
      <path class="dash-outline" d="M67 527 V449 H29 L107 370 L185 449 H152 V540"/>
      <polygon points="107,380 167,444 142,444 142,539 72,512 72,444 47,444" fill="var(--orange)"/>
      <text class="sans mid" x="107" y="359" font-size="22" fill="var(--ink)">1,307</text>
      <text class="sans mid" font-size="15" fill="var(--ink)"><tspan x="107" y="562">Road traffic</tspan><tspan x="107" y="581">accident deaths</tspan></text>
    </g>
    <g class="arrow-unintentional">
      <path class="dash-outline" d="M202 455 V367 H162 L239 289 L317 367 H282 V425"/>
      <polygon points="239,302 302,362 272,362 272,427 207,457 207,362 177,362" fill="var(--navy)"/>
      <text class="sans mid" x="239" y="278" font-size="22" fill="var(--ink)">2,091</text>
      <text class="sans mid" font-size="15" fill="var(--ink)"><tspan x="239" y="486">Unintentional</tspan><tspan x="239" y="505">Overdose Deaths</tspan></text>
    </g>
    <g class="arrow-all">
      <path class="dash-outline" d="M327 340 V297 H295 L372 217 L450 297 H412 V350"/>
      <polygon points="372,229 432,292 407,292 407,357 332,387 332,292 312,292" fill="var(--blue)"/>
      <text class="sans mid" x="372" y="205" font-size="22" fill="var(--ink)">2,596</text>
      <text class="sans mid" font-size="15" fill="var(--ink)"><tspan x="372" y="412">All drug</tspan><tspan x="372" y="431">induced deaths</tspan></text>
    </g>
  </svg>
</section>

<!-- Gender split -->
<section class="sheet col-1 row-2">
  <svg viewBox="0 0 480 678" aria-labelledby="t4">
    <text class="title" id="t4"><tspan x="240" y="84" class="it">Gender split of</tspan><tspan x="240" y="102">unintentional overdose deaths</tspan></text>
    <rect x="68" y="393" width="170" height="16" fill="var(--blue)"/>
    <polygon points="68,378 36,401 68,424" fill="var(--blue)"/>
    <circle cx="233" cy="347" r="70" fill="none" stroke="var(--blue)" stroke-width="17"/>
    <path d="M233 277 A70 70 0 0 1 299 371" fill="none" stroke="var(--orange)" stroke-width="17"/>
    <rect x="240" y="286" width="168" height="16" fill="var(--orange)"/>
    <polygon points="405,270 432,294 405,318" fill="var(--orange)"/>
    <circle cx="233" cy="281" r="11" fill="#fff"/>
    <text class="sans mid" x="233" y="286" font-size="13" fill="var(--ink)">F</text>
    <circle cx="277" cy="400" r="11" fill="#fff"/>
    <text class="sans mid" x="277" y="405" font-size="13" fill="var(--ink)">M</text>
    <text class="ring-caption"><tspan x="233" y="338" class="it">Gender split of</tspan><tspan x="233" y="350">unintentional</tspan><tspan x="233" y="362">overdose deaths</tspan></text>
    <circle role="img" aria-label="Illustration of a man in a suit" cx="102" cy="342" r="42" fill="var(--blue)"/>
    <circle role="img" aria-label="Illustration of a woman in office wear" cx="366" cy="362" r="42" fill="var(--orange)"/>
    <text class="sans mid" x="103" y="284" font-size="17" fill="var(--ink)">1520</text>
    <text class="sans mid" x="368" y="428" font-size="17" fill="var(--ink)">571</text>
  </svg>
</section>

<!-- Age groups -->
<section class="sheet col-2 row-2">
  <svg viewBox="0 0 480 678" aria-labelledby="t5">
    <text class="title" id="t5"><tspan x="240" y="84" class="it">Percent of unintentional</tspan><tspan x="240" y="102">overdose deaths by age group</tspan></text>
    <g class="y-axis">
      <line class="grid" x1="50" y1="280" x2="452" y2="280"/>
      <line class="grid" x1="50" y1="322" x2="452" y2="322"/>
      <line class="grid" x1="50" y1="364" x2="452" y2="364"/>
      <line class="grid" x1="50" y1="406" x2="452" y2="406"/>
      <line class="grid" x1="50" y1="448" x2="452" y2="448"/>
      <line class="grid" x1="50" y1="490" x2="452" y2="490"/>
      <line x1="50" y1="532" x2="452" y2="532" stroke="#9a9a9a" stroke-width="0.8"/>
      <text class="axis-label" x="28" y="283">25.5</text>
      <text class="axis-label" x="28" y="325">25.4</text>
      <text class="axis-label" x="28" y="367">17.1</text>
      <text class="axis-label" x="28" y="409">13.4</text>
      <text class="axis-label" x="34" y="451">9</text>
      <text class="axis-label" x="30" y="493">8.6</text>
      <text class="axis-label" x="30" y="535">0.8</text>
    </g>
    <g class="bars">
      <rect x="65" y="517" width="38" height="15" fill="#4a6fbd"/>
      <rect x="121" y="499" width="38" height="33" fill="#77c2d4"/>
      <rect x="177" y="443" width="38" height="89" fill="var(--slate)"/>
      <rect x="234" y="324" width="38" height="208" fill="var(--sky)"/>
      <rect x="289" y="282" width="38" height="250" fill="var(--slate)"/>
      <rect x="345" y="407" width="38" height="125" fill="#66a6dd"/>
      <rect x="398" y="449" width="38" height="83" fill="var(--teal-light)"/>
    </g>
    <g class="axis-label mid">
      <text x="84" y="546">0–19</text>
      <text x="140" y="546">20–29</text>
      <text x="196" y="546">30–39</text>
      <text x="253" y="546">40–49</text>
      <text x="308" y="546">50–59</text>
      <text x="364" y="546">60–69</text>
      <text x="417" y="546">70 years</text>
      <text x="417" y="556">and above</text>
    </g>
  </svg>
</section>

<!-- Indigenous rates -->
<section class="sheet col-3 row-2">
  <svg viewBox="0 0 480 678" aria-labelledby="t6">
    <text class="title" id="t6"><tspan x="240" y="86">Overdose death rates for</tspan><tspan x="240" y="104" class="it">Indigenous and non-Indigenous Australians</tspan></text>
    <line x1="69" y1="185" x2="69" y2="504" stroke="#555" stroke-width="0.8"/>
    <line x1="69" y1="504" x2="430" y2="504" stroke="#555" stroke-width="0.8"/>
    <g class="axis-label" text-anchor="end">
      <text x="58" y="192">30</text><text x="58" y="213">28</text><text x="58" y="234">26</text>
      <text x="58" y="256">24</text><text x="58" y="277">22</text><text x="58" y="298">20</text>
      <text x="58" y="319">18</text><text x="58" y="340">16</text><text x="58" y="362">14</text>
      <text x="58" y="383">12</text><text x="58" y="404">10</text><text x="58" y="425">8</text>
      <text x="58" y="446">6</text><text x="58" y="468">4</text><text x="58" y="489">2</text>
    </g>
    <g class="axis-label mid">
      <text x="89" y="517">2014</text><text x="122" y="517">2015</text><text x="156" y="517">2016</text>
      <text x="189" y="517">2017</text><text x="222" y="517">2018</text><text x="256" y="517">2019</text>
      <text x="289" y="517">2020</text><text x="322" y="517">2021</text><text x="355" y="517">2022</text>
      <text x="389" y="517">2023</text><text x="422" y="517">2024</text>
    </g>
    <polyline points="89,363 122,333 156,321 189,318 222,325 256,295 289,313 322,301 355,274 389,281 422,197" fill="none" stroke="var(--orange)" stroke-width="2"/>
    <polyline points="89,443 122,437 156,437 189,435 222,434 256,438 289,439 322,440 355,440 389,445 422,437" fill="none" stroke="var(--blue)" stroke-width="2"/>
    <g fill="#2a0d0d">
      <circle cx="89" cy="363" r="3.5"/><circle cx="122" cy="333" r="3.5"/><circle cx="156" cy="321" r="3.5"/>
      <circle cx="189" cy="318" r="3.5"/><circle cx="222" cy="325" r="3.5"/><circle cx="256" cy="295" r="3.5"/>
      <circle cx="289" cy="313" r="3.5"/><circle cx="322" cy="301" r="3.5"/><circle cx="355" cy="274" r="3.5"/>
      <circle cx="389" cy="281" r="3.5"/><circle cx="422" cy="197" r="3.5"/>
      <circle cx="89" cy="443" r="3.5"/><circle cx="122" cy="437" r="3.5"/><circle cx="156" cy="437" r="3.5"/>
      <circle cx="189" cy="435" r="3.5"/><circle cx="222" cy="434" r="3.5"/><circle cx="256" cy="438" r="3.5"/>
      <circle cx="289" cy="439" r="3.5"/><circle cx="322" cy="440" r="3.5"/><circle cx="355" cy="440" r="3.5"/>
      <circle cx="389" cy="445" r="3.5"/><circle cx="422" cy="437" r="3.5"/>
    </g>
    <g class="point-label">
      <text x="82" y="353">13.6</text><text x="116" y="320">16.4</text><text x="149" y="316">17.6</text>
      <text x="184" y="313">17.9</text><text x="218" y="345">17.2</text><text x="254" y="289">20</text>
      <text x="284" y="328">18.3</text><text x="319" y="296">19.5</text><text x="352" y="267">22</text>
      <text x="386" y="298">21.3</text><text x="418" y="189">29.3</text>
      <text x="86" y="457">6.1</text><text x="118" y="429">6.6</text><text x="152" y="429">6.6</text>
      <text x="184" y="427">6.8</text><text x="219" y="426">6.9</text><text x="251" y="452">6.5</text>
      <text x="285" y="454">6.4</text><text x="318" y="455">6.3</text><text x="350" y="455">6.3</text>
      <text x="385" y="461">5.9</text><text x="417" y="428">6.6</text>
    </g>
    <rect x="150" y="546" width="7" height="7" fill="var(--orange)"/>
    <text class="sans" x="167" y="553" font-size="10" fill="var(--ink)">Indigenous</text>
    <rect x="233" y="546" width="7" height="7" fill="var(--blue)"/>
    <text class="sans" x="249" y="553" font-size="10" fill="var(--ink)">Non–Indigenous</text>
  </svg>
</section>

<!-- Opioid types -->
<section class="sheet col-1 row-3">
  <svg viewBox="0 0 480 678" aria-labelledby="t7">
    <text class="title" id="t7" x="240" y="86">Deaths by <tspan class="it">opioid types</tspan></text>
    <g fill="none" stroke="#f3f3f3" stroke-width="2">
      <circle cx="190" cy="323" r="162"/><circle cx="190" cy="323" r="136"/>
      <circle cx="190" cy="323" r="117"/><circle cx="190" cy="323" r="99"/>
    </g>
    <g fill="none" stroke-width="7" stroke-linecap="round">
      <path d="M190 467 A144 144 0 0 1 55.9 270.5" stroke="var(--navy)"/>
      <path d="M190 449 A126 126 0 0 1 109.4 419.9" stroke="var(--violet)"/>
      <path d="M190 431 A108 108 0 1 1 245.6 230.4" stroke="var(--green)"/>
      <path d="M190 413 A90 90 0 1 1 189.9 233" stroke="var(--orange)"/>
      <path d="M190 396 A73 73 0 1 1 263 323" stroke="var(--blue)"/>
      <path d="M190 380 A57 57 0 0 1 133 323" stroke="var(--maroon)"/>
    </g>
    <g class="leader">
      <polyline points="198,380 360,380 360,362"/>
      <polyline points="198,396 417,396 417,375"/>
      <polyline points="198,413 355,413"/>
      <polyline points="198,431 403,431 403,445"/>
      <polyline points="198,449 330,449 330,462"/>
      <polyline points="198,467 262,467 262,478"/>
    </g>
    <g class="tiny">
      <text x="345" y="345">Synthetics (inc. fentanyl,</text>
      <text x="345" y="352">pethidine, tramadol)</text>
      <text x="383" y="371">Pharmaceutical opioids</text>
      <text x="359" y="410">Natural and semi-synthetics (inc.</text>
      <text x="359" y="417">oxycodone, morphine, codeine)</text>
      <text x="385" y="452">Total opioids</text>
      <text x="315" y="469">Methadone</text>
      <text x="254" y="486">Heroin</text>
    </g>
    <g class="sans mid" font-size="10" fill="var(--ink)">
      <text x="62" y="260">488</text>
      <text x="262" y="247">877</text>
      <text x="211" y="238">236</text>
      <text x="135" y="310">194</text>
      <text x="261" y="343">370</text>
      <text x="91" y="407">160</text>
    </g>
  </svg>
</section>

<!-- Polydrug -->
<section class="sheet col-2 row-3">
  <svg viewBox="0 0 480 678" aria-labelledby="t8">
    <text class="title" id="t8"><tspan x="240" y="86" class="it">Polydrug vs single</tspan><tspan x="240" y="104">drug deaths 2020-2024</tspan></text>
    <g fill="none" stroke="var(--ink)" stroke-width="1.8">
      <path d="M202 193 H191 V273"/>
      <path d="M287 193 H299 V273"/>
      <path d="M87 329 V301 Q87 281 107 281 H160"/>
      <path d="M87 423 V450 Q87 470 107 470 H187"/>
      <path d="M401 329 V301 Q401 281 381 281 H328"/>
      <path d="M401 423 V450 Q401 470 381 470 H300"/>
    </g>
    <g fill="var(--ink)">
      <circle cx="202" cy="193" r="3.5"/><circle cx="287" cy="193" r="3.5"/>
      <circle cx="87" cy="329" r="3.5"/><circle cx="87" cy="423" r="3.5"/>
      <circle cx="401" cy="329" r="3.5"/><circle cx="401" cy="423" r="3.5"/>
    </g>
    <circle cx="244" cy="374" r="104" fill="var(--navy)"/>
    <text class="hub-title"><tspan x="244" y="358" class="it">Polydrug vs</tspan><tspan x="244" y="377"><tspan class="it">single</tspan> drug deaths</tspan><tspan x="244" y="396">2020-2024</tspan></text>
    <circle cx="245" cy="214" r="38" fill="var(--violet)"/>
    <text class="sans mid" x="245" y="200" font-size="7.5" fill="#fff">Single</text>
    <text class="sans mid" x="245" y="209" font-size="7.5" fill="#fff">Drug Type</text>
    <text class="sans mid" x="245" y="231" font-size="18" fill="#fff">2,354</text>
    <circle cx="88" cy="376" r="38" fill="var(--blue)"/>
    <text class="sans mid" x="88" y="362" font-size="7.5" fill="#fff">Two</text>
    <text class="sans mid" x="88" y="371" font-size="7.5" fill="#fff">Drug Types</text>
    <text class="sans mid" x="88" y="393" font-size="18" fill="#fff">1,340</text>
    <circle cx="401" cy="376" r="38" fill="var(--orange)"/>
    <text class="sans mid" x="401" y="362" font-size="7.5" fill="#fff">Three or more</text>
    <text class="sans mid" x="401" y="371" font-size="7.5" fill="#fff">Drug Type</text>
    <text class="sans mid" x="401" y="393" font-size="18" fill="#fff">3,610</text>
  </svg>
</section>

<!-- Drug type -->
<section class="sheet col-3 row-3">
  <svg viewBox="0 0 480 678" aria-labelledby="t9">
    <text class="title" id="t9"><tspan x="243" y="86">Unintentional</tspan><tspan x="243" y="104" class="it">deaths by drug type</tspan></text>
    <g fill="var(--track)">
      <rect x="127.5" y="134" width="9" height="402"/><rect x="151.5" y="134" width="9" height="402"/>
      <rect x="175.5" y="134" width="9" height="402"/><rect x="199.5" y="134" width="9" height="402"/>
      <rect x="225.5" y="134" width="9" height="402"/><rect x="249.5" y="134" width="9" height="402"/>
      <rect x="275.5" y="134" width="9" height="402"/><rect x="299.5" y="134" width="9" height="402"/>
      <rect x="325.5" y="134" width="9" height="402"/>
    </g>
    <g stroke-width="7" stroke-linecap="round">
      <line x1="132" y1="164" x2="132" y2="508" stroke="var(--orange)"/>
      <line x1="156" y1="209" x2="156" y2="508" stroke="var(--violet)"/>
      <line x1="180" y1="234" x2="180" y2="508" stroke="var(--blue)"/>
      <line x1="204" y1="279" x2="204" y2="508" stroke="var(--navy)"/>
      <line x1="230" y1="306" x2="230" y2="508" stroke="var(--charcoal)"/>
      <line x1="254" y1="331" x2="254" y2="508" stroke="var(--purple)"/>
      <line x1="280" y1="349" x2="280" y2="508" stroke="var(--maroon)"/>
      <line x1="304" y1="371" x2="304" y2="508" stroke="var(--green)"/>
      <line x1="330" y1="416" x2="330" y2="508" stroke="var(--blue)"/>
    </g>
    <g class="axis-label" font-size="9">
      <text transform="translate(136 156) rotate(-90)">877</text>
      <text transform="translate(160 201) rotate(-90)">772</text>
      <text transform="translate(184 226) rotate(-90)">514</text>
      <text transform="translate(208 271) rotate(-90)">311</text>
      <text transform="translate(234 298) rotate(-90)">293</text>
      <text transform="translate(258 323) rotate(-90)">234</text>
      <text transform="translate(284 341) rotate(-90)">218</text>
      <text transform="translate(308 363) rotate(-90)">174</text>
      <text transform="translate(334 408) rotate(-90)">141</text>
    </g>
    <line x1="349" y1="134" x2="349" y2="536" stroke="#bbb" stroke-width="0.8"/>
    <line x1="120" y1="536" x2="352" y2="536" stroke="#bbb" stroke-width="0.8"/>
    <g stroke="#bbb" stroke-width="0.8">
      <line x1="345" y1="160" x2="349" y2="160"/><line x1="345" y1="220" x2="349" y2="220"/>
      <line x1="345" y1="280" x2="349" y2="280"/><line x1="345" y1="340" x2="349" y2="340"/>
      <line x1="345" y1="400" x2="349" y2="400"/><line x1="345" y1="460" x2="349" y2="460"/>
    </g>
    <g class="axis-label" font-size="9">
      <text transform="translate(136 636) rotate(-90)">Opioids</text>
      <text transform="translate(160 636) rotate(-90)">Amphetamine</text>
      <text transform="translate(184 636) rotate(-90)">Benzodiazepines</text>
      <text transform="translate(208 636) rotate(-90)">Alcohol</text>
      <text transform="translate(234 636) rotate(-90)">Antidepressants</text>
      <text transform="translate(258 636) rotate(-90)">Anti-convulsants</text>
      <text transform="translate(284 636) rotate(-90)">Cannabinoids</text>
      <text transform="translate(308 636) rotate(-90)">Antipsychotics</text>
      <text transform="translate(334 636) rotate(-90)">Cocaine</text>
    </g>
  </svg>
</section>

</body>
</html>
```